Women's Health Company needs business card

We need a business card for a USA based women's health care company. We use digital technology to enhance therapy prescribed by clinicians for their patients

```html
<!DOCTYPE html>
<html lang="en">
<head>
<meta charset="utf-8">
<title>Lunara Health – Business Card</title>
<link href="https://fonts.googleapis.com/css2?family=Montserrat:wght@400;500;800&display=swap" rel="stylesheet">
<style>
  :root {
    --teal: #76bfbe;
    --teal-deep: #6bb6b5;
    --purple: #8b4fa6;
    --ink: #141414;
    --paper: #ffffff;
    --backdrop: #ececec;
  }
  * { box-sizing: border-box; margin: 0; padding: 0; }
  html, body { width: 1200px; height: 900px; overflow: hidden; }
  body {
    background: var(--backdrop);
    font-family: "Montserrat", sans-serif;
    position: relative;
  }
  .card {
    position: absolute;
    left: 285px;
    width: 630px;
    height: 360px;
    overflow: hidden;
    box-shadow: 0 6px 18px rgba(0,0,0,0.15);
  }
  .card--front { top: 70px; background: var(--teal); }
  .card--back { top: 470px; background: var(--teal); display: flex; align-items: center; justify-content: center; }
  .card__shape { position: absolute; inset: 0; width: 100%; height: 100%; }

  .wordmark {
    position: absolute;
    left: 52px;
    top: 58px;
    color: var(--teal-deep);
    font-weight: 500;
    font-size: 44px;
    line-height: 1;
    letter-spacing: 0.01em;
  }
  .wordmark__sub {
    display: block;
    font-size: 18px;
    letter-spacing: 0.55em;
    margin-top: 10px;
    padding-left: 60px;
  }
  .divider {
    position: absolute;
    left: 292px;
    top: 110px;
    width: 2px;
    height: 150px;
    background: var(--purple);
  }
  .contact {
    position: absolute;
    left: 318px;
    top: 98px;
    color: var(--ink);
    font-size: 14px;
    line-height: 1.35;
  }
  .contact__name {
    color: var(--purple);
    font-weight: 800;
    font-size: 22px;
    letter-spacing: 0.03em;
  }
  .contact__title { margin-bottom: 10px; }
  .contact__address { margin-bottom: 12px; }
  .contact__row { display: flex; align-items: center; gap: 8px; }
  .contact__icon { width: 14px; height: 14px; flex: none; }

  .wordmark--reverse {
    position: static;
    color: var(--paper);
    font-size: 78px;
    font-weight: 400;
    text-align: center;
  }
  .wordmark--reverse .wordmark__sub {
    font-size: 26px;
    padding-left: 0;
    margin-top: 14px;
    letter-spacing: 0.6em;
  }
</style>
</head>
<body>
  <section class="card card--front" aria-label="Business card front">
    <svg class="card__shape" viewBox="0 0 630 360" aria-hidden="true">
      <path d="M0,0 H630 V360 H555 C480,300 360,275 220,245 C120,224 50,180 20,80 C15,60 8,50 0,48 Z" fill="#ffffff"/>
      <path d="M42,150 C80,215 150,235 240,255 C360,282 460,305 540,345" fill="none" stroke="#8b4fa6" stroke-width="5" stroke-linecap="round"/>
    </svg>

    <div class="wordmark">Lunara<span class="wordmark__sub">HEALTH</span></div>

    <div class="divider"></div>

    <div class="contact">
      <p class="contact__name">MARISOL</p>
      <p class="contact__title">Co-Founder</p>
      <p class="contact__address">Brightwell Plaza 1200 Oak<br>Meadow Ave NW Suite 310</p>
      <p class="contact__row">
        <svg class="contact__icon" viewBox="0 0 16 16" aria-hidden="true"><path d="M3 2h3l1.5 3.5-2 1.2a8 8 0 0 0 3.8 3.8l1.2-2L14 10v3a1 1 0 0 1-1 1A11 11 0 0 1 2 3a1 1 0 0 1 1-1z" fill="#8b4fa6"/></svg>
        555-218-4630
      </p>
      <p class="contact__row">
        <svg class="contact__icon" viewBox="0 0 16 16" aria-hidden="true"><rect x="1" y="3" width="14" height="10" rx="1" fill="#8b4fa6"/><path d="M1.5 3.5 8 9l6.5-5.5" fill="none" stroke="#fff" stroke-width="1.2"/></svg>
        hello@lunarahealth.com
      </p>
      <p class="contact__row">
        <svg class="contact__icon" viewBox="0 0 16 16" aria-hidden="true"><circle cx="8" cy="8" r="7" fill="#8b4fa6"/><path d="M1 8h14M8 1c-3 3.5-3 10.5 0 14M8 1c3 3.5 3 10.5 0 14" fill="none" stroke="#fff" stroke-width="1"/></svg>
        www.lunarahealth.com
      </p>
    </div>
  </section>

  <section class="card card--back" aria-label="Business card back">
    <div class="wordmark wordmark--reverse">Lunara<span class="wordmark__sub">HEALTH</span></div>
  </section>
</body>
</html>
```